Meadow Crate Co came about when a life change having to do with my health became an issue and I had to change my diet. We’re a homeschool family and learned a more simplistic way to eat and live out our day to day. We’re ready to share how we eat. Included are attachments to give a visual to the concepts in mind. The first attachment is the logo the second is basically the main idea of the company referencing to getting to the roots of nutrition and juicing. The roots design CONCEPT would be incorporated onto the bottle label. The third attachment is representing the clear stickers we’d like to have on bottles. The 4th and Last are the bottle design we’re looking to use. We’d like tall cylinder bottles.

Label must haves :
meadow crate co logo and the quote know your roots
The roots design
MeadowCrateCo.example

```html
<!DOCTYPE html>
<html lang="en">
<head>
<meta charset="utf-8">
<title>Meadow Crate Co – Juice Label</title>
<link href="https://fonts.googleapis.com/css2?family=Montserrat:wght@500;600;700&display=swap" rel="stylesheet">
<style>
  :root {
    --bg: #f3f3f3;
    --label-light: #f0224a;
    --label-mid: #e01f46;
    --label-dark: #b81a3f;
    --ink: #ffffff;
    --band-grey: #9a9a9a;
    --logo-grey: #cfcfcf;
    --logo-ink: #7d7d7d;
    --url-grey: #9d9d9d;
  }
  * { margin: 0; padding: 0; box-sizing: border-box; }
  html, body { width: 1200px; height: 1058px; overflow: hidden; background: var(--bg); }
  body { position: relative; font-family: "Montserrat", sans-serif; color: var(--ink); }

  .label {
    position: absolute; top: 170px; width: 290px; height: 760px;
    border-radius: 120px 120px 28px 28px;
    background: radial-gradient(ellipse at 45% 40%, var(--label-light) 0%, var(--label-mid) 55%, var(--label-dark) 100%);
  }
  .label--front { left: 160px; }
  .label--back { left: 750px; }

  .roots-art {
    position: absolute; left: 64px; top: 204px; width: 150px; height: 206px;
    border-radius: 60px 60px 30px 30px;
    background: radial-gradient(ellipse at 50% 45%, rgba(255,255,255,0.45), rgba(255,255,255,0.12));
  }

  .tagline {
    position: absolute; left: 30px; top: 452px; width: 102px;
    font-weight: 700; font-size: 24px; line-height: 25px; text-align: right; letter-spacing: 0.3px;
  }
  .divider { position: absolute; left: 140px; width: 2px; background: var(--ink); }
  .divider--top { top: 452px; height: 76px; }
  .divider--bottom { top: 554px; height: 58px; }

  .brand {
    position: absolute; left: 150px; top: 438px; width: 92px; height: 92px;
    border-radius: 50%; background: var(--logo-grey);
    display: flex; align-items: center; justify-content: center; text-align: center;
  }
  .brand-name { font-weight: 700; font-size: 15px; line-height: 17px; color: var(--logo-ink); }

  .ingredients-front {
    position: absolute; left: 24px; top: 554px;
    font-weight: 600; font-size: 6.2px; line-height: 9px; letter-spacing: -0.2px; white-space: nowrap;
  }
  .badges { position: absolute; display: flex; }
  .badges span { border: 1.3px solid var(--ink); border-radius: 50%; }
  .badges--front { left: 24px; top: 589px; gap: 5px; }
  .badges--front span { width: 18px; height: 18px; }
  .badges--back { left: 50px; top: 416px; gap: 7px; }
  .badges--back span { width: 32px; height: 32px; border-width: 1.6px; }

  .product-type {
    position: absolute; left: 160px; top: 554px;
    font-weight: 700; font-size: 18.5px; line-height: 19px;
  }

  .url-band {
    position: absolute; height: 36px;
    display: flex; align-items: center; justify-content: center;
    font-weight: 700; font-size: 15.5px; white-space: nowrap;
  }
  .url-band--front { left: 30px; top: 626px; width: 222px; background: var(--band-grey); color: var(--ink); }
  .url-band--back { left: 40px; top: 618px; width: 224px; background: var(--ink); color: var(--url-grey); }

  .copy { position: absolute; left: 50px; white-space: nowrap; }
  .copy h2 { font-weight: 700; font-size: 11.5px; line-height: 14px; margin-bottom: 5px; }
  .copy p { font-weight: 500; font-size: 8.2px; line-height: 9.7px; letter-spacing: -0.1px; }
  .copy--one { top: 209px; }
  .copy--two { top: 328px; }

  .ingredients-back {
    position: absolute; left: 50px; top: 458px; white-space: nowrap;
    font-weight: 700; font-size: 8px; line-height: 12px; letter-spacing: -0.2px;
  }
  .closing {
    position: absolute; left: 45px; top: 528px; width: 200px; text-align: center; white-space: nowrap;
    font-weight: 700; font-size: 8.3px; line-height: 12px;
  }
</style>
</head>
<body>

<section class="label label--front">
  <div class="roots-art" role="img" aria-label="Illustration of a tree whose roots form a pair of lungs, white line art"></div>

  <div class="tagline">KNOW YOUR ROOTS</div>
  <div class="divider divider--top"></div>

  <div class="brand">
    <div class="brand-name">Meadow<br>Crate<br>Co</div>
  </div>

  <p class="ingredients-front">Beetroot, Spirulina, Chlorella,<br>Mushrooms, Pre &amp; Probiotics,<br>Veggies, Vitamins &amp; More!</p>
  <div class="badges badges--front" aria-hidden="true">
    <span></span><span></span><span></span><span></span><span></span>
  </div>

  <div class="divider divider--bottom"></div>
  <div class="product-type">Cold<br>Preseed<br>Juice</div>

  <div class="url-band url-band--front">MeadowCrateCo.example</div>
</section>

<section class="label label--back">
  <div class="copy copy--one">
    <h2>Lorem ipsum</h2>
    <p>Lorem ipsum dolor sit amet, consectetuer<br>adipiscing elit, sed diam nonummy nibh euismod<br>tincidunt ut laoreet dolore magna aliquam erat<br>volutpat. Ut wisi enim ad minim veniam, quis<br>nostrud exerci tation ullamcorper suscipit lobortis<br>nisl ut aliquip ex ea commodo consequat. Duis<br>autem vel eum iriure dolor in hendrerit in<br>vulputate velit esse molestie consequat, vel illum<br>dolore eu feugiat nulla facilisis.</p>
  </div>
  <div class="copy copy--two">
    <h2>Lorem ipsum</h2>
    <p>Lorem ipsum dolor sit amet, consectetuer<br>adipiscing elit, sed diam nonummy nibh euismod<br>tincidunt ut laoreet dolore magna aliquam erat<br>volutpat. Ut wisi enim ad minim veniam, quis<br>nostrud exerci tation ullamcorper suscipit lobortis<br>nisl ut aliquip ex ea commodo consequat.</p>
  </div>

  <div class="badges badges--back" aria-hidden="true">
    <span></span><span></span><span></span><span></span><span></span>
  </div>

  <p class="ingredients-back">Beetroot, Spirulina, Chlorella, Mushrooms,<br>Pre &amp; Probiotics, Veggies, Vitamins &amp; More!</p>

  <p class="closing">Lorem ipsum dolor sit amet,<br>consectetuer adipiscing elit, sed<br>diam nonummy nibh euismod<br>tincidunt ut laoreet dolore</p>

  <div class="url-band url-band--back">MeadowCrateCo.example</div>
</section>

</body>
</html>
```